Firm Stationery Design

I need a design for stationery, including: Stationery First Page, Stationery Second Sheet, Envelope, Mailing Label for Flat Envelopes, and Business Cards

```html
<!DOCTYPE html>
<html lang="en">
<head>
<meta charset="utf-8">
<title>Marlow Law LLC — Business Card</title>
<link href="https://fonts.googleapis.com/css2?family=Raleway:wght@700;800&family=Roboto:wght@400&display=swap" rel="stylesheet">
<style>
  :root {
    --backdrop: #e6e7e8;
    --paper: #ffffff;
    --ink: #1a1a1a;
    --accent: #f6a01a;
    --text-grey: #4d4d4d;
    --back-dark: #0b0b0b;
    --back-mid: #3a3a3a;
    --back-light: #8a8a8a;
  }
  * { margin: 0; padding: 0; box-sizing: border-box; }
  html, body { width: 1200px; height: 1000px; overflow: hidden; background: var(--backdrop); }
  .canvas { position: relative; width: 1200px; height: 1000px; }

  .card { position: absolute; left: 284px; width: 633px; height: 361px; overflow: hidden; }
  .card-front { top: 127px; background: var(--paper); }
  .card-back { top: 511px; background: var(--back-dark); }

  .name-bar {
    position: absolute; left: 0; top: 48px; width: 316px; height: 68px;
    background: var(--ink); padding: 11px 0 0 57px;
  }
  .person-name {
    font-family: 'Raleway', sans-serif; font-weight: 800; font-size: 23px;
    color: #fff; letter-spacing: 0.2px; line-height: 26px;
  }
  .person-title {
    font-family: 'Raleway', sans-serif; font-weight: 700; font-size: 15px;
    color: var(--accent); line-height: 20px;
  }

  .firm-name {
    position: absolute; left: 324px; top: 58px; height: 50px;
    display: flex; align-items: center; gap: 12px;
  }
  .firm-square { width: 44px; height: 50px; background: var(--accent); }
  .firm-wordmark {
    font-family: 'Raleway', sans-serif; font-weight: 800; font-size: 30px;
    color: var(--ink); letter-spacing: 0.5px;
  }

  .contact-list {
    position: absolute; left: 56px; top: 245px; list-style: none;
    font-family: 'Roboto', sans-serif; font-size: 17.5px; color: var(--text-grey);
  }
  .contact-list li { display: flex; align-items: center; height: 24.5px; }
  .contact-list svg { width: 17px; height: 17px; margin-right: 10px; fill: var(--accent); }

  .address {
    position: absolute; right: 60px; top: 248px; text-align: right;
    font-family: 'Roboto', sans-serif; font-size: 17.5px; line-height: 24.5px; color: var(--text-grey);
  }

  .footer-band { position: absolute; left: 0; bottom: 0; width: 100%; height: 20px; display: flex; }
  .footer-band .band-dark { width: 404px; background: var(--ink); }
  .footer-band .band-accent { flex: 1; background: var(--accent); }

  .back-pattern {
    position: absolute; inset: 0;
    background: radial-gradient(ellipse at 10% 5%, var(--back-light) 0%, var(--back-mid) 35%, var(--back-dark) 75%);
  }
  .back-mark {
    position: absolute; left: 483px; top: 222px; width: 66px; height: 62px;
    display: flex; align-items: center; justify-content: center; background: var(--back-dark);
    font-family: 'Raleway', sans-serif; font-weight: 800; font-size: 12px; color: #fff; letter-spacing: 0.3px;
  }
</style>
</head>
<body>
<div class="canvas">

  <section class="card card-front">
    <div class="name-bar">
      <p class="person-name">DARREN HOLLOWAY</p>
      <p class="person-title">Founder &amp; CEO</p>
    </div>

    <div class="firm-name">
      <span class="firm-square"></span>
      <span class="firm-wordmark">MARLOW LAW LLC</span>
    </div>

    <ul class="contact-list">
      <li>
        <svg viewBox="0 0 24 24" aria-hidden="true"><path d="M4 9c0-3 3.5-5 8-5s8 2 8 5v2h-4V9.5c-1-.6-2.4-1-4-1s-3 .4-4 1V11H4V9zm3 3h10l2 8H5l2-8zm5 2a2.5 2.5 0 100 5 2.5 2.5 0 000-5z"/></svg>
        (520) 555-0147
      </li>
      <li>
        <svg viewBox="0 0 24 24" aria-hidden="true"><path d="M2 6h20v2l-10 6L2 8V6zm0 4.3l10 6 10-6V19H2v-8.7z"/></svg>
        info@marlowlawllc.com
      </li>
      <li>
        <svg viewBox="0 0 24 24" aria-hidden="true"><path d="M12 2a10 10 0 100 20 10 10 0 000-20zm-1 3c-.5 1.5-2.5 2-2 4s3 1 3 3-2 2-1.5 4 1.5 2.5 1 4.5A7.9 7.9 0 014.3 9.5C6 8 8 6 11 5zm4 2c1 0 2.5 1 3.5 2.5.5 1 .5 2.5-.5 3s-2-.5-2.5 1-1 2-2 1.5 0-2.5-.5-3.5-1.5-1-1.5-2.5S14 7 15 7z"/></svg>
        www.marlowlawllc.com
      </li>
    </ul>

    <p class="address">480 Seaview Ave Suite 210,<br>Bayside Beach,<br>90000 California / USA</p>

    <div class="footer-band"><span class="band-dark"></span><span class="band-accent"></span></div>
  </section>

  <section class="card card-back">
    <div class="back-pattern" role="img" aria-label="Embossed repeating brand-mark pattern fading from grey to black"></div>
    <div class="back-mark">MARLOW</div>
  </section>

</div>
</body>
</html>
```